Small environmental consultancy requires basic yet awesome website design by aspiring and cool desig

We are a small environmental consultancy based in Australia, we have set-out a design brief for our website, using a logo we had completed here on Pixel Harbor as well. We hope you can help us with a website!

Website must be wordpress friendly - we have reserved hosting with them already!

Number of Pages Required

4 page

Requirements
Must have
• use supplied logo
• wordpress
• follow provided brief

```html
<!DOCTYPE html>
<html lang="en">
<head>
<meta charset="utf-8">
<title>Verdant Advisory – Environmental Consultancy</title>
<link href="https://fonts.googleapis.com/css2?family=Open+Sans:wght@400;600;700;800&display=swap" rel="stylesheet">
<style>
:root{
  --green:#8cc63f;
  --green-dark:#6fa52c;
  --ink:#333;
  --muted:#777;
  --line:#e3e3e3;
  --footer:#2e2e2e;
  --footer-bar:#232323;
  --sky-top:#eef3f6;
  --sky-bottom:#cfe0c2;
}
*{box-sizing:border-box;margin:0;padding:0}
html,body{width:1200px;height:2612px;overflow:hidden}
body{font-family:"Open Sans",Arial,sans-serif;color:var(--ink);background:#fff;position:relative;font-size:13px}
.abs{position:absolute}

/* header */
.site-header{left:0;top:0;width:1200px;height:118px;background:#fff}
.brand{left:120px;top:22px;display:flex;align-items:center;gap:10px}
.brand-dot{width:44px;height:44px;border-radius:50%;background:var(--green)}
.brand-name{font-weight:700;font-size:20px;color:var(--green-dark);line-height:1.1}
.topline{right:170px;top:18px;font-size:12px;color:var(--muted)}
.topline b{color:var(--ink);font-size:15px;margin-left:10px}
.main-nav{right:170px;top:56px;display:flex;gap:4px}
.main-nav a{display:block;padding:10px 16px;font-size:13px;color:var(--ink);text-decoration:none;border:1px solid var(--line);background:#fafafa}
.main-nav a.active{background:var(--green);color:#fff;border-color:var(--green)}

/* hero */
.hero{left:0;top:118px;width:1200px;height:390px;background:linear-gradient(180deg,var(--sky-top) 0%,#f6f8f5 55%,var(--sky-bottom) 100%)}
.hero-photo{left:600px;top:0;width:600px;height:390px;background:radial-gradient(ellipse at 55% 55%,#d8b79c 0%,#e6efe0 45%,transparent 70%)}
.hero-copy{left:176px;top:110px}
.hero-copy .pre{font-size:30px;font-weight:600;letter-spacing:2px;color:#444}
.hero-copy h1{font-size:50px;font-weight:800;letter-spacing:2px;color:#222;line-height:1}
.hero-copy .sub{font-size:13px;font-weight:700;color:#444;margin-top:6px;letter-spacing:1px}
.hero-copy p{width:300px;font-size:12px;color:var(--muted);margin-top:10px;line-height:1.5}
.btn{display:inline-block;background:var(--green);color:#fff;font-size:11px;font-weight:700;padding:10px 22px;border-radius:20px;text-transform:uppercase}
.hero-copy .btn{background:#fff;color:var(--ink);border:1px solid #ccc;margin-top:24px}

/* gallery */
.gallery{left:176px;top:520px;width:848px;display:grid;grid-template-columns:repeat(4,200px);gap:16px 16px}
.tile{height:176px;border:5px solid #fff;box-shadow:0 2px 6px rgba(0,0,0,.2)}
.t1{background:linear-gradient(#a9b8c4,#6f7c70)}
.t2{background:linear-gradient(#c7a07a,#6b7d5a)}
.t3{background:linear-gradient(#b8cde0,#4e7b3c)}
.t4{background:linear-gradient(#d9d7cf,#6a6a5a)}
.t5{background:linear-gradient(#9fa6a4,#4f5a4b)}
.t6{background:linear-gradient(#bcd4e8,#6b9c3f)}
.t7{background:linear-gradient(#aab1b7,#5f5f5a)}
.t8{background:linear-gradient(#8fa07c,#556b3f)}

/* welcome */
.welcome{left:0;top:960px;width:1200px;height:540px;background:linear-gradient(180deg,#f3f6f2 0%,#e4ead6 60%,#d4dcc0 100%)}
.welcome-photo{left:160px;top:60px;width:320px;height:420px;background:linear-gradient(180deg,#e9ecec 0%,#c9cf9f 60%,#9aa56c 100%)}
.welcome-card{left:560px;top:80px;width:480px;height:400px;background:rgba(255,255,255,.9);padding:30px}
.welcome-card .pre{font-size:16px;color:var(--green-dark);font-weight:600;letter-spacing:1px}
.welcome-card h2{font-size:28px;font-weight:800;color:var(--green);letter-spacing:1px;line-height:1.1}
.welcome-card p{font-size:12px;color:var(--muted);line-height:1.6;margin-top:14px}
.welcome-card .btn{margin-top:26px}

/* services + people */
.section-title{font-size:14px;font-weight:700;color:var(--green-dark);text-transform:uppercase;padding-bottom:6px;border-bottom:2px solid var(--green)}
.services{left:168px;top:1560px;width:260px}
.services ul{list-style:none;margin-top:10px;border:1px solid var(--line)}
.services li{font-size:12px;padding:11px 14px;border-bottom:1px solid var(--line);color:#555;display:flex;gap:8px;align-items:center}
.services li:before{content:"";width:6px;height:6px;border-radius:50%;background:var(--green)}
.services li.head{background:var(--green);color:#fff;font-weight:700;text-transform:uppercase}
.services li.head:before{background:#fff}
.people{left:472px;top:1560px;width:568px}
.person{display:flex;gap:18px;margin-top:16px;padding-bottom:14px;border-bottom:1px solid var(--line)}
.portrait{width:150px;height:150px;background:linear-gradient(#c9b9a6,#6d6f74);flex:none}
.person h3{font-size:14px;font-weight:700}
.person .role{font-size:11px;color:var(--green-dark);margin:2px 0 8px}
.person p{font-size:11.5px;color:var(--muted);line-height:1.55}
.person .more{font-size:11px;color:var(--green-dark);margin-top:8px;display:block}

/* partners */
.partners{left:168px;top:2000px;width:872px;display:grid;grid-template-columns:repeat(5,156px);gap:22px 23px}
.partner{height:90px;background:#fff;border:1px solid var(--line);display:flex;align-items:center;justify-content:center;box-shadow:0 1px 4px rgba(0,0,0,.08)}
.partner span{width:90px;height:36px;background:#d7dde0;border-radius:4px}
.partners-band{left:0;top:1960px;width:1200px;height:330px;background:linear-gradient(180deg,#fff 0%,#eef2ea 100%)}

/* footer */
.site-footer{left:0;top:2290px;width:1200px;height:322px;background:var(--footer);color:#bbb}
.f-col{top:30px}
.f-col h4{font-size:13px;color:#fff;font-weight:700;text-transform:uppercase;padding-bottom:8px;border-bottom:1px solid #555;margin-bottom:12px}
.f-col p{font-size:11.5px;line-height:1.7}
.f-contact{left:168px;width:240px}
.f-about{left:480px;width:260px}
.f-brand{left:820px;top:40px;width:220px;text-align:center}
.f-brand .brand-row{display:flex;align-items:center;justify-content:center;gap:10px}
.f-brand .brand-dot{width:40px;height:40px}
.f-brand .brand-name{color:#fff;font-size:20px}
.socials{display:flex;gap:10px;justify-content:center;margin-top:26px}
.socials span{width:22px;height:22px;border-radius:50%;background:#555}
.footer-bar{left:0;top:244px;width:1200px;height:78px;background:var(--footer-bar);font-size:11.5px}
.footer-bar nav{position:absolute;left:168px;top:30px;display:flex;gap:22px}
.footer-bar nav a{color:#bbb;text-decoration:none}
.footer-bar .copy{position:absolute;left:820px;top:30px;color:#999}
</style>
</head>
<body>

<header class="site-header abs">
  <div class="brand abs"><span class="brand-dot"></span><span class="brand-name">Verdant<br>Advisory</span></div>
  <div class="topline abs">Email: hello@verdantadvisory.example <b>Call Us : 0400 555 123</b></div>
  <nav class="main-nav abs">
    <a class="active" href="#">Home</a><a href="#">About Us</a><a href="#">Services</a><a href="#">People</a><a href="#">Clients</a><a href="#">Contact Us</a>
  </nav>
</header>

<section class="hero abs">
  <div class="hero-photo abs" role="img" aria-label="Cupped hands holding a young green seedling in soil"></div>
  <div class="hero-copy abs">
    <div class="pre">ENVIRONMENTAL</div>
    <h1>CONSULTANCY</h1>
    <div class="sub">BASED IN AUSTRALIA</div>
    <p>Practical environmental advice for projects of every size, from early planning through approvals and ongoing site care.</p>
    <span class="btn">Learn more</span>
  </div>
</section>

<div class="gallery abs">
  <div class="tile t1" role="img" aria-label="Solar panel array on site"></div>
  <div class="tile t2" role="img" aria-label="Team meeting outdoors"></div>
  <div class="tile t3" role="img" aria-label="Green field with wind turbine"></div>
  <div class="tile t4" role="img" aria-label="Worker inspecting equipment"></div>
  <div class="tile t5" role="img" aria-label="Industrial plant structures"></div>
  <div class="tile t6" role="img" aria-label="Person in open green meadow"></div>
  <div class="tile t7" role="img" aria-label="Power station cooling towers"></div>
  <div class="tile t8" role="img" aria-label="Field crew working in bushland"></div>
</div>

<section class="welcome abs">
  <div class="welcome-photo abs" role="img" aria-label="Site engineer in hard hat reviewing plans in a field"></div>
  <div class="welcome-card abs">
    <div class="pre">WELCOME TO</div>
    <h2>ENVIRONMENTAL CONSULTANCY</h2>
    <p>We help developers, councils and landholders understand their environmental obligations and meet them with confidence. Our small team brings hands-on field experience and clear reporting to every job.</p>
    <p>From flora and fauna surveys to management plans and approvals, we work alongside you to find sensible outcomes that protect the land and keep projects moving forward on time.</p>
    <p>Get in touch to talk about your next project and how we can support it.</p>
    <span class="btn">Read more</span>
  </div>
</section>

<section class="services abs">
  <div class="section-title">Services</div>
  <ul>
    <li class="head">Project Management</li>
    <li>Risk appraisal</li>
    <li>Site environmental plans</li>
    <li>Technical specifications</li>
    <li>Tendering support</li>
    <li>Flora and fauna surveys</li>
    <li>Land rehabilitation</li>
  </ul>
</section>

<section class="people abs">
  <div class="section-title">People</div>
  <div class="person">
    <div class="portrait" role="img" aria-label="Portrait of Liam Carter"></div>
    <div>
      <h3>Liam Carter</h3>
      <div class="role">Principal Consultant</div>
      <p>Liam leads our field programs and has spent many years guiding projects through environmental review. He works closely with clients to plan practical, well documented outcomes.</p>
      <span class="more">Read more</span>
    </div>
  </div>
  <div class="person">
    <div class="portrait" role="img" aria-label="Portrait of Noah Bennett"></div>
    <div>
      <h3>Noah Bennett</h3>
      <div class="role">Senior Ecologist</div>
      <p>Noah specialises in ecological survey and habitat management. He brings careful fieldwork and clear advice to every assessment he delivers for our clients.</p>
      <span class="more">Read more</span>
    </div>
  </div>
</section>

<div class="partners-band abs"></div>
<div class="partners abs">
  <div class="partner"><span></span></div><div class="partner"><span></span></div><div class="partner"><span></span></div><div class="partner"><span></span></div><div class="partner"><span></span></div>
  <div class="partner"><span></span></div><div class="partner"><span></span></div><div class="partner"><span></span></div><div class="partner"><span></span></div><div class="partner"><span></span></div>
</div>

<footer class="site-footer abs">
  <div class="f-col f-contact abs">
    <h4>Contact Info</h4>
    <p>Verdant Advisory<br>12 Sample Court, Greenvale QLD 4000<br>PO Box 321, Greenvale QLD 4000<br>hello@verdantadvisory.example<br>Phone No: 0400 555 123<br>Phone No: 0400 555 456</p>
  </div>
  <div class="f-col f-about abs">
    <h4>About Us</h4>
    <p>A small consultancy offering clear, practical environmental advice across the region.</p>
    <p>We partner with clients to plan, assess and manage sites responsibly from start to finish.</p>
  </div>
  <div class="f-brand abs">
    <div class="brand-row"><span class="brand-dot"></span><span class="brand-name">Verdant Advisory</span></div>
    <div class="socials"><span></span><span></span><span></span><span></span><span></span></div>
  </div>
  <div class="footer-bar abs">
    <nav><a href="#">Home</a><a href="#">Services</a><a href="#">People</a><a href="#">Clients</a><a href="#">Contact Us</a></nav>
    <div class="copy">© Copyright 2015 Verdant Advisory. All Rights Reserved.</div>
  </div>
</footer>

</body>
</html>
```